Rehearsal studio business card design needed

My rehearsal studio i bought not that long ago was opened as a hobby originally and was definitely not taken seriously. I am trying to make the new look studio be launched with the new look business cards. I am looking for very simple and clean look cards to match the simple and clean studios. the colour scheme is red and grey. over all i am really just looking for a very simple card that is not too busy and just gets the point accross.
Target Market(s)
Targeting bands, music teachers, students, etc.
Industry/Entity Type
Business
Contact Information for Business Card
Bayridge Sound Centre
Rehearsal and Recording Facilities
Owen Barlow CEO
unit 8, 47 Garvin Road Tallow NSW 2093
0491 382 905
bayridgesoundcentre@mailvex.com
Requirements
Must have
- simplicity
Nice to have

```html
<!DOCTYPE html>
<html lang="en">
<head>
<meta charset="utf-8">
<title>Bayridge Sound Centre – Business Card</title>
<link href="https://fonts.googleapis.com/css2?family=Ropa+Sans&display=swap" rel="stylesheet">
<style>
  :root {
    --page: #ffffff;
    --card: #080909;
    --red: #b3191c;
    --cyan: #5fc6d6;
    --white: #f4f4f4;
  }
  html, body {
    margin: 0;
    padding: 0;
    width: 1200px;
    height: 1000px;
    overflow: hidden;
    background: var(--page);
  }
  .canvas {
    position: relative;
    width: 1200px;
    height: 1000px;
    font-family: "Ropa Sans", "Arial Narrow", sans-serif;
    color: var(--white);
  }
  .card {
    position: absolute;
    top: 339px;
    width: 545px;
    height: 316px;
    background: var(--card);
  }
  .card--front { left: 16px; }
  .card--back { left: 641px; }

  .frame {
    position: absolute;
    box-sizing: border-box;
  }
  .frame--outer {
    left: 7px; top: 8px; right: 8px; bottom: 8px;
    border: 3px solid var(--red);
  }
  .frame--inner {
    left: 19px; top: 21px; right: 21px; bottom: 21px;
    border: 2px solid var(--cyan);
  }

  .brand {
    position: absolute;
    left: 0; right: 0;
    top: 56px;
    display: flex;
    flex-direction: column;
    align-items: center;
  }
  .brand__mark {
    width: 100px;
    height: 100px;
  }
  .brand__name {
    margin-top: 52px;
    font-size: 30px;
    letter-spacing: 0.5px;
    color: var(--white);
    line-height: 1;
  }

  .details {
    position: absolute;
    left: 0; right: 0;
    top: 50px;
    text-align: center;
  }
  .details__company {
    margin: 0;
    font-size: 27px;
    font-weight: 400;
    letter-spacing: 0.6px;
    line-height: 32px;
  }
  .details__tagline {
    margin: 2px 0 0;
    font-size: 17px;
    letter-spacing: 0.4px;
    line-height: 22px;
  }
  .details__contact {
    margin: 33px 0 0;
    font-size: 20px;
    letter-spacing: 0.5px;
    line-height: 31px;
    font-style: normal;
  }
</style>
</head>
<body>
<main class="canvas">
  <section class="card card--front" aria-label="Card front">
    <div class="frame frame--outer"></div>
    <div class="frame frame--inner"></div>
    <div class="brand">
      <svg class="brand__mark" viewBox="0 0 100 100" aria-hidden="true">
        <circle cx="50" cy="50" r="48" fill="#b3191c"/>
      </svg>
      <div class="brand__name">Bayridge Sound Centre</div>
    </div>
  </section>

  <section class="card card--back" aria-label="Card back">
    <div class="details">
      <h1 class="details__company">Bayridge Sound Centre</h1>
      <p class="details__tagline">Rehearsal and Recording Facilities</p>
      <address class="details__contact">
        Owen Barlow CEO unit 8,<br>
        47 Garvin Road Tallow NSW<br>
        2093 0491 382 905<br>
        bayridgesoundcentre@mailvex.com
      </address>
    </div>
  </section>
</main>
</body>
</html>
```